Labour Day banner showcasing 20% off site

Banner graphic promoting our Labour Day sale
Size: 2000px x 600px
- examples from other companies and their sale banners have been uploaded for inspiration. Labour day examples are for the United States's holiday and submissions should NOT be in their country colours.
- product images can be found at www.tallpinegreens.com

Target Market(s)

19+

Industry/Entity Type

Cannabis

Requirements
Must have
• Phrases:
- “Happy Labour Day”
- “20% off site wide sale*"
- "Coupon code: Harvest20"
- Underneath phrase the date of sale “September 3rd - 7th”
- In tiny print “*excludes all sale and bundled items”
- MUST BE 2000px x 600px
Nice to have
• - images of the products or bud we carry which can be found at www.tallpinegreens.com
- bold
Should not have
• - company logo
- the American flag, we are a Canadian company, colours and flag should all be Canadian

```html
<!DOCTYPE html>
<html lang="en">
<head>
<meta charset="utf-8">
<title>Happy Labour Day – Site Wide Sale</title>
<link href="https://fonts.googleapis.com/css2?family=Montserrat:wght@600;700;800&family=Oswald:wght@500;600&display=swap" rel="stylesheet">
<style>
  :root {
    --navy-deep: #0a1f38;
    --navy-mid: #15416b;
    --red: #d9192b;
    --red-dark: #a80f1e;
    --blue: #1163d6;
    --blue-dark: #0b48a8;
    --cyan: #19a4f4;
    --white: #ffffff;
    --balloon-red: rgba(222, 34, 48, 0.95);
    --balloon-white: rgba(238, 236, 240, 0.95);
    --bud-green: #7a9440;
    --bud-olive: #5a6e2c;
    --bud-amber: #b07a34;
    --bud-dark: #33421c;
  }
  html, body { margin: 0; padding: 0; overflow: hidden; }
  .banner {
    position: relative;
    width: 1200px;
    height: 360px;
    overflow: hidden;
    background: radial-gradient(ellipse 65% 80% at 50% 30%, var(--navy-mid) 0%, #0f2f52 55%, var(--navy-deep) 100%);
    font-family: "Montserrat", sans-serif;
  }
  .balloons {
    position: absolute;
    top: 0;
    height: 360px;
    background-repeat: no-repeat;
  }
  .balloons--left {
    left: 0;
    width: 240px;
    background:
      radial-gradient(circle 32px at 58px 40px, var(--balloon-red) 0 40%, var(--balloon-white) 41% 55%, var(--balloon-red) 56% 70%, transparent 72%),
      radial-gradient(circle 16px at 125px 65px, var(--balloon-white) 0 70%, transparent 72%),
      radial-gradient(circle 20px at 113px 128px, var(--balloon-red) 0 35%, var(--balloon-white) 36% 55%, var(--balloon-red) 56% 70%, transparent 72%),
      radial-gradient(circle 45px at 28px 95px, var(--balloon-white) 0 68%, transparent 72%),
      radial-gradient(circle 52px at 55px 160px, var(--balloon-red) 0 68%, transparent 72%),
      radial-gradient(circle 48px at 105px 230px, var(--balloon-red) 0 30%, var(--balloon-white) 31% 50%, var(--balloon-red) 51% 70%, transparent 72%),
      radial-gradient(circle 48px at 30px 265px, var(--balloon-white) 0 68%, transparent 72%),
      radial-gradient(circle 50px at 175px 310px, rgba(222,34,48,0.75) 0 66%, transparent 72%),
      radial-gradient(circle 50px at 90px 330px, var(--balloon-red) 0 30%, var(--balloon-white) 31% 50%, var(--balloon-red) 51% 70%, transparent 72%);
  }
  .balloons--right {
    right: 0;
    width: 220px;
    background:
      radial-gradient(circle 14px at 157px 6px, var(--balloon-red) 0 70%, transparent 72%),
      radial-gradient(circle 30px at 212px 35px, var(--balloon-red) 0 35%, var(--balloon-white) 36% 55%, var(--balloon-red) 56% 70%, transparent 72%),
      radial-gradient(circle 30px at 133px 55px, var(--balloon-white) 0 68%, transparent 72%),
      radial-gradient(circle 20px at 103px 105px, var(--balloon-red) 0 35%, var(--balloon-white) 36% 55%, var(--balloon-red) 56% 70%, transparent 72%),
      radial-gradient(circle 33px at 185px 105px, var(--balloon-red) 0 68%, transparent 72%),
      radial-gradient(circle 40px at 95px 170px, var(--balloon-red) 0 30%, var(--balloon-white) 31% 50%, var(--balloon-red) 51% 70%, transparent 72%),
      radial-gradient(circle 45px at 168px 185px, var(--balloon-white) 0 68%, transparent 72%),
      radial-gradient(circle 55px at 110px 265px, var(--balloon-red) 0 68%, transparent 72%),
      radial-gradient(circle 52px at 60px 335px, var(--balloon-red) 0 30%, var(--balloon-white) 31% 50%, var(--balloon-red) 51% 70%, transparent 72%),
      radial-gradient(circle 52px at 195px 320px, var(--balloon-red) 0 30%, var(--balloon-white) 31% 50%, var(--balloon-red) 51% 70%, transparent 72%),
      radial-gradient(circle 28px at 140px 335px, var(--balloon-white) 0 68%, transparent 72%);
  }
  .bud {
    position: absolute;
    background:
      radial-gradient(ellipse 30% 35% at 35% 40%, rgba(176,122,52,0.7), transparent 70%),
      radial-gradient(ellipse 25% 30% at 70% 55%, rgba(176,122,52,0.55), transparent 70%),
      radial-gradient(ellipse at 45% 40%, var(--bud-green) 0%, var(--bud-olive) 55%, var(--bud-dark) 100%);
    filter: drop-shadow(0 6px 8px rgba(0,0,0,0.45));
  }
  .bud--left {
    left: 177px; top: 138px; width: 132px; height: 76px;
    border-radius: 40% 60% 45% 55% / 55% 45% 60% 40%;
    transform: rotate(-6deg);
  }
  .bud--right {
    left: 900px; top: 143px; width: 126px; height: 80px;
    border-radius: 55% 45% 60% 40% / 45% 55% 45% 55%;
    transform: rotate(14deg);
  }
  .graphic { position: absolute; inset: 0; }
  .ribbon-text { font-family: "Montserrat", sans-serif; font-weight: 600; letter-spacing: 5px; }
  .headline { font-family: "Montserrat", sans-serif; font-weight: 800; }
  .deal { font-family: "Oswald", sans-serif; font-weight: 600; }
  .sale-line { font-family: "Oswald", sans-serif; font-weight: 500; }
  .date-line { font-family: "Montserrat", sans-serif; font-weight: 700; }
  .coupon-label { font-family: "Montserrat", sans-serif; font-weight: 700; }
  .coupon-code { font-family: "Montserrat", sans-serif; font-weight: 800; }
  .fine-print {
    position: absolute; left: 793px; top: 340px;
    color: var(--white); font-size: 9.6px; font-weight: 600; margin: 0;
  }
</style>
</head>
<body>
<main class="banner">
  <div class="balloons balloons--left" role="img" aria-label="Cluster of red and white heart and striped balloons with maple leaves and silver confetti"></div>
  <div class="balloons balloons--right" role="img" aria-label="Cluster of red and white heart and striped balloons with maple leaves and silver confetti"></div>
  <div class="bud bud--left" role="img" aria-label="Photo of a cannabis flower bud"></div>
  <div class="bud bud--right" role="img" aria-label="Photo of a cannabis flower bud"></div>

  <svg class="graphic" viewBox="0 0 1200 360" width="1200" height="360">
    <polygon class="ribbon" points="528,24 670,24 664,37 670,51 528,51 534,37" fill="var(--red)"/>
    <polygon points="528,48 670,48 668,51 530,51" fill="var(--red-dark)"/>
    <text class="ribbon-text" x="600" y="44" text-anchor="middle" font-size="18" fill="var(--white)">HAPPY</text>
    <text class="headline" x="601" y="99" text-anchor="middle" font-size="48" fill="var(--white)">LABOUR DAY</text>

    <polygon class="frame" points="450,161 722,120 722,281 450,322" fill="none" stroke="var(--white)" stroke-width="1.4"/>
    <line x1="408" y1="182" x2="594" y2="154" stroke="var(--cyan)" stroke-width="1" stroke-dasharray="3 2"/>
    <line x1="666" y1="268" x2="722" y2="260" stroke="var(--cyan)" stroke-width="1" stroke-dasharray="3 2"/>

    <polygon class="band-tail" points="414,304 624,272 624,308 495,346 514,300" fill="var(--blue)"/>
    <polygon class="band" points="408,192 756,134 756,262 408,303" fill="var(--blue)"/>
    <polygon class="band-date" points="513,231 714,203 692,237 513,267" fill="var(--blue-dark)"/>
    <polygon class="percent-box" points="401,196 514,181 514,277 401,291" fill="var(--cyan)"/>
    <polygon points="401,291 514,277 514,281 405,294" fill="var(--blue-dark)"/>

    <g transform="rotate(-4 460 240)">
      <text class="deal" x="410" y="270" font-size="76" fill="var(--white)" textLength="57" lengthAdjust="spacingAndGlyphs">20</text>
      <text class="deal" x="472" y="228" font-size="26" fill="var(--white)" textLength="18" lengthAdjust="spacingAndGlyphs">%</text>
      <text class="deal" x="471" y="259" font-size="34" fill="var(--white)" textLength="36" lengthAdjust="spacingAndGlyphs">OFF</text>
    </g>

    <text class="sale-line" transform="translate(525 213) rotate(-9.4)" font-size="29" fill="var(--white)" textLength="206">SITE WIDE SALE*</text>
    <text class="date-line" transform="translate(531 254) rotate(-9.4)" font-size="18" fill="var(--white)">September 3<tspan font-size="10" dy="-7">rd</tspan><tspan dy="7"> - 7</tspan><tspan font-size="10" dy="-7">th</tspan></text>

    <path d="M779,308 Q784,330 770,360" fill="none" stroke="var(--white)" stroke-width="0.8"/>
    <g transform="rotate(-8 771 258)">
      <path class="heart" d="M771,309 C735,280 712,258 714,236 C716,216 734,206 750,210 C762,213 768,221 771,228 C774,221 780,213 792,210 C808,206 826,216 828,236 C830,258 807,280 771,309 Z" fill="var(--red)"/>
      <text class="coupon-label" x="771" y="240" text-anchor="middle" font-size="8.5" fill="var(--white)">Coupon code:</text>
      <text class="coupon-code" x="771" y="259" text-anchor="middle" font-size="14" fill="var(--white)">Harvest20</text>
    </g>
  </svg>

  <p class="fine-print">* Excludes all sale &amp; bundled items</p>
</main>
</body>
</html>
```